Business Card Design

We're a new real estate investment company based out of West Palm Beach Florida. We buy distressed properties to fix and flip. We want the color scheme of the card to match the colors of our logo which is black and gold. We encourage all designers to be creative with the design of the card. We are not looking for a bland, boring, traditional business card. Please use legible fonts for the text as well.

Target Market(s)

Home owners, and Real Estate Investors.

Industry/Entity Type

Real Estate

Contact Information for Business Card

Dalen Vorstagg
Real Estate Investor

ESTATE FALCONS, LLC
7248 S. CORAL HAVEN WAY
SUITE 19
WEST PALM BEACH, FL. 33162
OFFICE: 1-800-555-0182
FAX: 1-888-555-0147
EMAIL: dalen@estatefalcons.example
www.estatefalcons.example

Requirements
Must have
• PLACE THESE WORDS IN BIG BOLD PRINT ON BOTH SIDES OF THE DESIGN:

WE BUY HOUSES WITH CASH!

```html
<!DOCTYPE html>
<html lang="en">
<head>
<meta charset="utf-8">
<title>Estate Falcons, LLC — Business Card</title>
<link rel="stylesheet" href="https://fonts.googleapis.com/css2?family=Exo+2:ital,wght@0,700;0,800;1,800&family=Open+Sans:wght@400;600&display=swap">
<style>
  :root {
    --ink: #0b0b0b;
    --gold: #f2d516;
    --gold-deep: #d9b80c;
    --lime: #a9cf3c;
    --paper: #f1f1f1;
    --paper-shade: #dcdcdc;
    --white: #ffffff;
    --stage: #e6e4e0;
  }
  * { box-sizing: border-box; margin: 0; padding: 0; }
  html, body { width: 1200px; height: 1200px; overflow: hidden; }
  body {
    background: var(--stage);
    font-family: "Open Sans", Arial, sans-serif;
    position: relative;
  }
  .card {
    position: absolute;
    left: 100px;
    width: 1000px;
    height: 560px;
    overflow: hidden;
    box-shadow: 0 8px 24px rgba(0,0,0,.18);
  }

  /* ---------- Front ---------- */
  .card--front { top: 30px; background: linear-gradient(180deg, var(--paper), #e9e9e9); }
  .front-band { position: absolute; inset: 0; width: 100%; height: 100%; }
  .front-deco {
    position: absolute;
    background: radial-gradient(ellipse at center, var(--paper-shade) 0%, rgba(220,220,220,.5) 55%, rgba(241,241,241,0) 75%);
  }
  .front-deco--left { left: 40px; top: 150px; width: 380px; height: 400px; }
  .front-deco--right { right: -120px; top: 110px; width: 340px; height: 360px; }
  .front-mark {
    position: absolute;
    top: 150px; left: 0; right: 0;
    display: flex; justify-content: center; align-items: center; gap: 14px;
  }
  .front-mark__square { width: 34px; height: 34px; background: var(--ink); }
  .front-mark__name {
    font-family: "Exo 2", Arial, sans-serif;
    font-weight: 800;
    font-size: 34px;
    color: var(--ink);
    letter-spacing: 1px;
  }
  .front-title {
    position: absolute;
    top: 245px; left: 0; right: 0;
    text-align: center;
    font-family: "Exo 2", Arial, sans-serif;
    font-weight: 800;
    font-style: italic;
    font-size: 60px;
    color: var(--ink);
    letter-spacing: 1px;
  }
  .front-tagline {
    position: absolute;
    top: 345px; left: 0; right: 0;
    text-align: center;
    font-family: "Exo 2", Arial, sans-serif;
    font-weight: 800;
    font-size: 34px;
    color: var(--ink);
    letter-spacing: 1.5px;
  }
  .front-tagline span {
    background: var(--gold);
    padding: 6px 22px;
  }

  /* ---------- Back ---------- */
  .card--back { top: 620px; background: var(--ink); color: var(--white); }
  .back-curve { position: absolute; left: 470px; top: 0; width: 230px; height: 560px; }
  .back-illustration {
    position: absolute; left: 485px; top: 0; width: 110px; height: 250px;
    border-radius: 0 0 55px 55px;
    background: linear-gradient(180deg, var(--gold) 0%, var(--gold-deep) 100%);
  }
  .back-portrait {
    position: absolute; right: 0; top: 0; width: 360px; height: 560px;
    background: radial-gradient(ellipse at 55% 30%, #3b3b44 0%, #1d2233 45%, #121624 75%, var(--ink) 100%);
  }
  .back-company {
    position: absolute; left: 60px; top: 60px;
    font-family: "Exo 2", Arial, sans-serif;
    font-weight: 800; font-size: 38px; letter-spacing: 1px;
  }
  .back-tagline {
    position: absolute; left: 92px; top: 108px;
    font-family: "Exo 2", Arial, sans-serif;
    font-weight: 800; font-size: 22px; color: var(--gold); letter-spacing: 1px;
  }
  .back-name {
    position: absolute; left: 60px; top: 190px;
    font-family: "Exo 2", Arial, sans-serif;
    font-weight: 700; font-size: 32px; color: var(--lime); letter-spacing: 1.5px;
  }
  .back-role {
    position: absolute; left: 60px; top: 232px; width: 420px;
    font-size: 20px; color: var(--gold); letter-spacing: .5px;
    padding-bottom: 6px; border-bottom: 2px solid var(--white);
  }
  .back-address {
    position: absolute; left: 50px; top: 282px;
    font-size: 20px; line-height: 30px; letter-spacing: .3px;
  }
  .contact-list { position: absolute; left: 40px; top: 375px; list-style: none; }
  .contact-list li {
    display: flex; align-items: center; gap: 16px;
    font-size: 23px; height: 42px; letter-spacing: .5px;
  }
  .contact-list svg { width: 26px; height: 26px; flex: none; }
</style>
</head>
<body>

<section class="card card--front" aria-label="Card front">
  <div class="front-deco front-deco--left" role="img" aria-label="Faint lion head illustration"></div>
  <div class="front-deco front-deco--right" role="img" aria-label="Faint lion head illustration"></div>
  <svg class="front-band" viewBox="0 0 1000 560" preserveAspectRatio="none" aria-hidden="true">
    <path d="M0 0 H1000 V45 C860 15 700 25 520 55 C330 85 160 115 0 150 Z" fill="var(--ink)"/>
    <path d="M0 150 C160 115 330 85 520 55 C700 25 860 15 1000 45" fill="none" stroke="var(--gold)" stroke-width="10"/>
  </svg>
  <div class="front-mark">
    <span class="front-mark__square"></span>
    <span class="front-mark__name">ESTATE FALCONS</span>
  </div>
  <h1 class="front-title">ESTATE FALCONS, LLC</h1>
  <p class="front-tagline"><span>WE BUY HOUSES WITH CASH!</span></p>
</section>

<section class="card card--back" aria-label="Card back">
  <div class="back-portrait" role="img" aria-label="Portrait photo of the investor in a dark suit"></div>
  <div class="back-illustration" role="img" aria-label="Gold lion profile illustration"></div>
  <svg class="back-curve" viewBox="0 0 230 560" aria-hidden="true">
    <path d="M70 250 C80 360 150 450 195 560" fill="none" stroke="var(--gold)" stroke-width="10"/>
  </svg>

  <div class="back-company">ESTATE FALCONS, LLC</div>
  <div class="back-tagline">WE BUY HOUSES WITH CASH!</div>

  <div class="back-name">DALEN VORSTAGG</div>
  <div class="back-role">REAL ESTATE INVESTOR</div>
  <div class="back-address">7248 S. CORAL HAVEN WAY SUITE 19 WEST<br>PALM BEACH, FL. 33162</div>

  <ul class="contact-list">
    <li>
      <svg viewBox="0 0 24 24" aria-hidden="true"><path fill="var(--gold)" d="M6.6 10.8c1.4 2.8 3.8 5.1 6.6 6.6l2.2-2.2c.3-.3.7-.4 1-.2 1.1.4 2.3.6 3.6.6.6 0 1 .4 1 1V20c0 .6-.4 1-1 1C10.6 21 3 13.4 3 4c0-.6.4-1 1-1h3.5c.6 0 1 .4 1 1 0 1.3.2 2.5.6 3.6.1.3 0 .7-.2 1z"/></svg>
      <span>1-800-555-0182</span>
    </li>
    <li>
      <svg viewBox="0 0 24 24" aria-hidden="true"><path fill="var(--gold)" d="M6 3h12v5H6zM3 9h18v8h-3v4H6v-4H3zm5 6v4h8v-4z"/></svg>
      <span>1-888-555-0147</span>
    </li>
    <li>
      <svg viewBox="0 0 24 24" aria-hidden="true"><path fill="var(--gold)" d="M2 5h20v14H2zm2 2v.4l8 5.2 8-5.2V7z"/></svg>
      <span>dalen@estatefalcons.example</span>
    </li>
    <li>
      <svg viewBox="0 0 24 24" aria-hidden="true"><circle cx="12" cy="12" r="9" fill="none" stroke="var(--gold)" stroke-width="2"/><path d="M3 12h18M12 3c3 3 3 15 0 18M12 3c-3 3-3 15 0 18" fill="none" stroke="var(--gold)" stroke-width="1.6"/></svg>
      <span>www.estatefalcons.example</span>
    </li>
  </ul>
</section>

</body>
</html>
```